Tall Harbor Business Card

We are a Video Production and Video Equipment Rental company specialising in the supply of state of the art Video Technology and Services for the Live Entertainment, Television and Corporate Business Theatre markets. (in Sydney, Australia) www.tallharbor.example

Industry/Entity Type

Business

Contact Information for Business Card

name, position, email, website, address, logo
Example attached of the information we need - doesn't necessarily have to look the same

Font styles to use
Other font styles liked:
• Tall Harbor logo font is GOTHAM

Colors
ea1f27

Requirements
Nice to have
• either matt black or shiny black cards -
raised logo

```html
<!DOCTYPE html>
<html lang="en">
<head>
<meta charset="utf-8">
<title>Tall Harbor Business Card</title>
<link href="https://fonts.googleapis.com/css2?family=Marcellus&family=Marcellus+SC&display=swap" rel="stylesheet">
<style>
  :root {
    --brand-red: #ea1f27;
    --card-black: #050505;
    --paper-white: #ffffff;
    --text-white: #f4f4f4;
    --backdrop: #ffffff;
  }
  * { margin: 0; padding: 0; box-sizing: border-box; }
  html, body {
    width: 1200px;
    height: 1000px;
    overflow: hidden;
    background: var(--backdrop);
  }
  .business-card {
    position: absolute;
    left: 240px;
    top: 300px;
    width: 720px;
    height: 400px;
    display: flex;
    font-family: "Marcellus", serif;
  }
  .card-brand-side {
    position: relative;
    width: 330px;
    height: 100%;
    background: var(--brand-red);
    color: var(--text-white);
  }
  .brand-name {
    position: absolute;
    top: 78px;
    left: 0;
    width: 100%;
    text-align: center;
    font-family: "Marcellus", serif;
    font-size: 36px;
    letter-spacing: 1px;
    color: var(--paper-white);
  }
  .service-list {
    position: absolute;
    top: 168px;
    left: 92px;
    list-style: none;
    font-size: 19px;
    line-height: 1.25;
  }
  .service-list li::before {
    content: "\2016";
    margin-right: 2px;
  }
  .card-contact-side {
    position: relative;
    flex: 1;
    height: 100%;
    background: var(--card-black);
    text-align: center;
  }
  .frame-line {
    position: absolute;
    left: 0;
    top: 0;
  }
  .person-name {
    position: absolute;
    top: 80px;
    width: 100%;
    font-family: "Marcellus SC", serif;
    font-size: 36px;
    color: var(--brand-red);
  }
  .person-role {
    position: absolute;
    top: 128px;
    width: 100%;
    font-family: "Marcellus SC", serif;
    font-size: 21px;
    letter-spacing: 1px;
    color: var(--text-white);
  }
  .postal-address {
    position: absolute;
    top: 190px;
    width: 100%;
    font-style: normal;
    font-size: 17px;
    line-height: 1.2;
    letter-spacing: 1px;
    color: var(--brand-red);
  }
  .web-address {
    position: absolute;
    top: 286px;
    width: 100%;
    font-size: 17px;
    color: var(--text-white);
  }
  .email-address {
    position: absolute;
    top: 312px;
    width: 100%;
    font-size: 17px;
    color: var(--brand-red);
  }
</style>
</head>
<body>
  <div class="business-card">
    <section class="card-brand-side">
      <div class="brand-name">Tall Harbor</div>
      <ul class="service-list">
        <li>Video Solutions</li>
        <li>Led Screens</li>
        <li>Camera Systems</li>
        <li>Projection</li>
      </ul>
    </section>
    <section class="card-contact-side">
      <svg class="frame-line" width="390" height="400" viewBox="0 0 390 400" aria-hidden="true">
        <polyline points="26,78 26,66 360,66 360,78" fill="none" stroke="#ea1f27" stroke-width="2"/>
        <polyline points="20,334 20,346 354,346 354,334" fill="none" stroke="#ea1f27" stroke-width="2"/>
      </svg>
      <div class="person-name">Leo Marchetti</div>
      <div class="person-role">Managing Director</div>
      <address class="postal-address">
        12 Keel Street<br>
        Marrick NSW 2099<br>
        Australia
      </address>
      <div class="web-address">www.tallharbor.example</div>
      <div class="email-address">Email: Leo@tallharbor.example</div>
    </section>
  </div>
</body>
</html>
```